design a construction company business card

Design business card around our logo. Card must have all the typical info: name, title, address, phone, email, business name, etc. Somewhere on the card I would like to see our motto "Grounded in trust... Driven by true craftsmanship." Consider adding a splash of bright orange to the card to complement the blues and silvers/grays in the logo. We are open to metallic inks, textures, etc. We would like to see options on both light and dark backgrounds. The font in the logo is Euro Technic Extended Regular.

```html
<!DOCTYPE html>
<html lang="en">
<head>
<meta charset="utf-8">
<title>Kestrel Contracting – Business Card</title>
<link href="https://fonts.googleapis.com/css2?family=Open+Sans:wght@400;600;800&display=swap" rel="stylesheet">
<style>
  :root {
    --bg: #2b2b2b;
    --card: #222223;
    --blue: #2a6fd6;
    --blue-deep: #1f3fa8;
    --silver: #a9a9ab;
    --motto: #4a4a4c;
    --white: #f2f2f2;
  }
  * { margin: 0; padding: 0; box-sizing: border-box; }
  html, body { width: 1200px; height: 895px; overflow: hidden; }
  body {
    background: var(--bg);
    font-family: "Open Sans", Arial, sans-serif;
    position: relative;
  }
  .card {
    position: absolute;
    width: 560px;
    height: 320px;
    background: var(--card);
    border-radius: 14px;
    box-shadow: 0 18px 40px rgba(0,0,0,.55);
    overflow: hidden;
  }
  .card--back { left: 110px; top: 80px; }
  .card--front { left: 530px; top: 495px; }

  /* back side */
  .back-brand {
    position: absolute;
    left: 0; right: 0; top: 118px;
    text-align: center;
  }
  .brand-name {
    font-weight: 800;
    font-size: 40px;
    letter-spacing: 4px;
    line-height: 1;
    text-transform: uppercase;
  }
  .brand-sub {
    font-weight: 800;
    font-size: 14px;
    letter-spacing: 6px;
    margin-top: 8px;
    text-transform: uppercase;
  }
  .back-brand .brand-name, .back-brand .brand-sub { color: var(--silver); }
  .motto {
    position: absolute;
    left: 0; right: 0; top: 238px;
    text-align: center;
    color: var(--motto);
    font-size: 15px;
    letter-spacing: .5px;
  }

  /* front side */
  .front-brand {
    position: absolute;
    left: 36px; top: 130px;
    width: 240px;
  }
  .front-brand .brand-name { color: var(--blue); font-size: 31px; letter-spacing: 3px; }
  .front-brand .brand-sub { color: var(--blue); font-size: 11px; letter-spacing: 3px; }
  .divider {
    position: absolute;
    left: 290px; top: 74px;
    width: 2px; height: 182px;
    background: var(--white);
  }
  .details {
    position: absolute;
    left: 312px; top: 62px;
    color: var(--white);
  }
  .person-name {
    color: var(--blue);
    font-weight: 800;
    font-size: 25px;
    letter-spacing: .5px;
    text-transform: uppercase;
    line-height: 1.05;
  }
  .person-title { font-size: 14px; margin-bottom: 14px; }
  .address { font-size: 13px; line-height: 1.4; margin-bottom: 14px; }
  .contact-list { list-style: none; font-size: 13px; line-height: 1.55; }
  .contact-list li { display: flex; align-items: center; gap: 8px; }
  .contact-list svg { width: 14px; height: 14px; flex: none; }
  .card-edge {
    position: absolute;
    left: 0; right: 0; bottom: 0;
    height: 6px;
    background: linear-gradient(90deg, var(--blue), var(--blue-deep));
  }
</style>
</head>
<body>

<section class="card card--back" aria-label="Card back">
  <div class="back-brand">
    <div class="brand-name">Kestrel</div>
    <div class="brand-sub">Contracting, Inc.</div>
  </div>
  <p class="motto">Grounded in trust... Driven by true craftsmanship</p>
</section>

<section class="card card--front" aria-label="Card front">
  <div class="front-brand">
    <div class="brand-name">Kestrel</div>
    <div class="brand-sub">Contracting, Inc.</div>
  </div>

  <div class="divider"></div>

  <div class="details">
    <h1 class="person-name">Marcus Ellery</h1>
    <p class="person-title">Founder &amp; CEO</p>
    <p class="address">48 Carden Row, Suite # B<br>Bristol, United Kingdom BS14QT</p>
    <ul class="contact-list">
      <li>
        <svg viewBox="0 0 14 14" aria-hidden="true"><rect x="3.5" y="1" width="7" height="12" rx="1.5" fill="none" stroke="var(--blue)" stroke-width="1.6"/><line x1="6" y1="10.8" x2="8" y2="10.8" stroke="var(--blue)" stroke-width="1.2"/></svg>
        123 555 0147
      </li>
      <li>
        <svg viewBox="0 0 14 14" aria-hidden="true"><rect x="1" y="3" width="12" height="9" rx="1" fill="none" stroke="var(--blue)" stroke-width="1.6"/><polyline points="3.5,7 6,9.5 10.5,5" fill="none" stroke="var(--blue)" stroke-width="1.6"/></svg>
        marcus.ellery@kcx.co.uk
      </li>
      <li>
        <svg viewBox="0 0 14 14" aria-hidden="true"><circle cx="7.5" cy="6" r="4" fill="none" stroke="var(--blue)" stroke-width="1.8"/><line x1="4.6" y1="8.9" x2="1.8" y2="12" stroke="var(--blue)" stroke-width="2"/></svg>
        www.kcx.co.uk
      </li>
    </ul>
  </div>

  <div class="card-edge"></div>
</section>

</body>
</html>
```